Business Card Design Project

Hello
I want a Simple Business card that uses the company logo that is easily reasonable but looks professional as I am an IT Services company and would look to share these cards with prospective clients.
The details are:
Kelvo Ridge Solutions
14 Marlow Crescent
Birmingham
B7 4QT
Telephone 0845 271 6049
I would like my name Gareth Wilcombe and my title Director on the card.
Target Market(s)
IT Professionals
Industry/Entity Type
Business

```html
<!DOCTYPE html>
<html lang="en">
<head>
<meta charset="utf-8">
<title>Kelvo Ridge Solutions – Business Card</title>
<link href="https://fonts.googleapis.com/css2?family=Open+Sans:wght@400;600&display=swap" rel="stylesheet">
<style>
  :root {
    --bg-top: #f4f4f4;
    --bg-bottom: #d9d9d9;
    --card: #ffffff;
    --ink: #2b2b2b;
    --ink-soft: #6a6a6a;
    --rule: #8cc63f;
    --lime: #d7e84a;
    --green: #4fb848;
    --yellow: #f5d431;
    --leaf: #8cc63f;
    --pale-lime: #c4dd3c;
    --icon: #8cc63f;
  }
  * { margin: 0; padding: 0; box-sizing: border-box; }
  html, body { width: 1200px; height: 1200px; overflow: hidden; }
  body {
    background: linear-gradient(160deg, var(--bg-top), var(--bg-bottom));
    font-family: "Open Sans", sans-serif;
    display: flex; align-items: center; justify-content: center;
  }
  .card {
    position: relative;
    width: 1000px; height: 620px;
    background: var(--card);
    box-shadow: 0 18px 40px rgba(0,0,0,0.14);
    overflow: hidden;
  }
  .brand {
    position: absolute; left: 70px; top: 270px;
    display: flex; align-items: center; gap: 18px;
  }
  .brand-dot {
    width: 46px; height: 46px; border-radius: 50%;
    background: var(--leaf);
  }
  .brand-name {
    font-size: 40px; font-weight: 600; color: var(--ink);
    letter-spacing: -0.5px;
  }
  .divider {
    position: absolute; left: 620px; width: 2px; background: var(--rule);
  }
  .divider-top { top: 0; height: 250px; }
  .divider-bottom { top: 290px; height: 300px; }
  .person {
    position: absolute; right: 400px; top: 140px; text-align: right;
  }
  .person-name { font-size: 30px; font-weight: 600; color: var(--ink); }
  .person-title { font-size: 22px; color: var(--ink-soft); margin-top: 2px; }
  .contact {
    position: absolute; left: 650px; top: 330px;
    font-size: 24px; color: var(--ink); line-height: 1.35;
  }
  .contact-row { display: flex; gap: 12px; align-items: flex-start; margin-bottom: 10px; }
  .contact-row svg { flex: 0 0 28px; margin-top: 3px; }
  .band {
    position: absolute; left: 0; right: 0; bottom: 0; height: 30px;
    display: flex;
  }
  .band span { height: 100%; }
  .band .lime { background: var(--lime); width: 13%; }
  .band .green { background: var(--green); width: 14%; }
  .band .yellow { background: var(--yellow); width: 14%; }
  .band .leaf { background: var(--leaf); width: 16%; }
  .band .pale { background: var(--pale-lime); flex: 1; }
</style>
</head>
<body>
  <div class="card">
    <div class="brand">
      <div class="brand-dot"></div>
      <div class="brand-name">Kelvo Ridge Solutions</div>
    </div>

    <div class="divider divider-top"></div>
    <div class="divider divider-bottom"></div>

    <div class="person">
      <div class="person-name">Gareth Wilcombe</div>
      <div class="person-title">Director</div>
    </div>

    <div class="contact">
      <div class="contact-row">
        <svg width="28" height="28" viewBox="0 0 28 28" aria-hidden="true">
          <circle cx="14" cy="14" r="14" fill="var(--icon)"/>
          <path d="M7 14 L14 8 L21 14 L19 14 L19 20 L9 20 L9 14 Z" fill="#fff"/>
        </svg>
        <div>14 Marlow Crescent,<br>Birmingham, B7 4QT</div>
      </div>
      <div class="contact-row">
        <svg width="28" height="28" viewBox="0 0 28 28" aria-hidden="true">
          <circle cx="14" cy="14" r="14" fill="var(--icon)"/>
          <rect x="10" y="7" width="8" height="14" rx="1.5" fill="#fff"/>
          <rect x="12" y="9" width="4" height="8" fill="var(--icon)"/>
        </svg>
        <div>0845 271 6049</div>
      </div>
    </div>

    <div class="band">
      <span class="lime"></span><span class="green"></span><span class="yellow"></span><span class="leaf"></span><span class="pale"></span>
    </div>
  </div>
</body>
</html>
```